依頼詳細
【未来の塾生へメッセージ】

・昨年度第3期生全員志望校合格
・過去3年の実績
ー青嶺高校毎年合格
ーその他進学実績、白浜高専、白浜高校、藤波高校、朝霧野工業、光陽工業専修、白浜緑丘、西千歳高校、白浜東萌、明徳学園、朝短附、琴葉女子、葉技大附属
・勉強が苦手な生徒から所謂進学校へ進む生徒まで、すべての生徒と卒業まで向き合ってきました。定員10人の小さい教室ながら、まさに3年間、生徒と肩を組むようにして勉強に取り組みました。

6月峰陵模試平均点(県平均) 247.8点
1月峰陵模試平均点(県平均) 265.3点
差17.5点

↑普通はこれくらいしか伸びないのですが↑

当塾では、

6月峰陵模試平均点(蒼翔舎生) 262点
1月峰陵模試平均点(蒼翔舎生) 317.8点
差55.8点

↑ここ強調して欲しい!↑

最も上がった生徒は、6月下野模試258点 → 入試得点開示391点

なので、

250点が400点に!特に、真ん中から上位の指導を得意としています!

①小学校から中学卒業まで継続的な指導が出来ること②ウィークリーテストを行っている理由、③授業を受けるだけではいけない、④テスト期間は何回でも通塾可能
といった蒼翔舎ならではの部分を強く打ち出していけたらと考えております。

学年末テスト後のタイミング(2月中旬から3月にかけて予定)で、新聞折込やポスティングを考えております。

新年度から授業料の改定を行うため、料金に関してはすべてアップするのではなく、
小学生16,200円(講習時期除く)
中1、中2生21,600円(講習時期除く)
中3生23,760円(講習時期除く)
のような書き方をお願いしたいです。

小学生に関しては、“勉強のやり方から学ぶ個別指導”を売りにし、中学生でつまづきやすいところを分かった上で、塾長が直接指導しています。小学生のお子さんを持つ方に訴える部分、中学生のお子さんを持つ方に訴える部分の2セクションを持ってきてほしいです。

塾のLINEや塾長YouTube、授業風景の写真もたくさん使ってください!
記載項目
・250点が400点に!真ん中から上位の指導を得意としています!
・今の勉強法で中学生活やっていけるか不安。本気で成績を上げたい生徒。
・塾長が全生徒を教えていますので、突然先生が変わったりすることが小学生から中学卒業までありません。継続した安心できる指導です!

学習塾蒼翔舎/〒000-0000 栃木県下野市桐ヶ丘48-7/電話0000-00-0000/ホームページhttps://www.soushousha-juku.example/本気で成績を上げたい子のための学習塾/料金などは付属のファイルから
サイズ
B4
ページ数
両面
希望イメージ
シンプル 複雑
単色 カラフル
暗い 明るい
日常 高級
遊び心 厳粛
未来的 伝統的
女性的 男性的
希望する色
赤系、黄・オレンジ系、水色系
納品ファイル
• 高解像度JPG (.jpg)
補足説明
■ 選んだ理由

3年間の実績の見せ方が、一番まとめっていて綺麗でしたので、採用させていただきました。

■ 提案者全員のお礼・コメント

ご提案ありがとうございました。

他にも気に入った提案がございましたので、随分と悩みました。

またチラシ作成をお願いする場合には、ご提案よろしくお願いします!

```html
<!DOCTYPE html>
<html lang="ja">
<head>
<meta charset="utf-8">
<title>蒼翔舎 生徒募集チラシ</title>
<link rel="stylesheet" href="https://fonts.googleapis.com/css2?family=Noto+Sans+JP:wght@400;500;700;900&display=swap">
<style>
:root{
  --red:#d8231b;
  --orange:#f08a12;
  --yellow:#f9c400;
  --blue:#1b4f9c;
  --ink:#2a2a2a;
  --grey:#6b6b6b;
  --paper:#ffffff;
}
*{margin:0;padding:0;box-sizing:border-box}
html,body{width:863px;height:1200px;overflow:hidden;background:var(--paper)}
body{font-family:"Noto Sans JP",sans-serif;color:var(--ink)}
.flyer{position:relative;width:863px;height:1200px;overflow:hidden;background:#fff}
.abs{position:absolute}

.hero-bg{left:0;top:0;width:863px;height:590px;background:linear-gradient(180deg,#eef3f7,#f7f8f9)}
.student-photo{left:480px;top:0;width:383px;height:590px;
  background:linear-gradient(160deg,#e7eef3 0%,#cdd9e2 55%,#b7c6d2 100%)}

.up-arrow{left:40px;top:60px;width:440px;height:200px}
.score-lead{left:130px;top:28px;padding:0 18px;background:#fff;border-radius:30px;
  color:var(--red);font-weight:900;font-size:32px;transform:rotate(-6deg);white-space:nowrap}
.score-big{left:130px;top:70px;font-weight:900;font-size:110px;line-height:1;color:var(--yellow);
  -webkit-text-stroke:5px var(--blue);paint-order:stroke fill;transform:rotate(-6deg);white-space:nowrap}
.score-big small{font-size:60px}
.score-ni{left:395px;top:108px;font-weight:900;font-size:44px;color:var(--blue);transform:rotate(-6deg)}
.score-up{left:320px;top:205px;font-weight:900;font-size:62px;line-height:1;color:var(--red);
  -webkit-text-stroke:4px #fff;paint-order:stroke fill;transform:rotate(-6deg)}

.headline{left:34px;top:340px;color:var(--red);font-weight:900;line-height:1.08;
  -webkit-text-stroke:6px #fff;paint-order:stroke fill;white-space:nowrap}
.headline .l1{font-size:64px}
.headline .l2{font-size:72px}
.headline .l3{font-size:45px}

.brand-rule{left:0;top:590px;width:863px;height:4px;background:var(--red)}
.brand{left:30px;top:606px;display:flex;align-items:center;gap:10px}
.brand-mark{width:40px;height:40px;background:var(--red)}
.brand-name{font-weight:900;font-size:40px;line-height:1;color:var(--ink);letter-spacing:3px}
.schools{left:250px;top:602px;display:flex;gap:8px}
.schools span{background:var(--blue);color:#fff;font-weight:700;font-size:17px;padding:1px 10px;white-space:nowrap}
.target{left:250px;top:634px;font-size:17px;font-weight:700;display:flex;align-items:center;gap:8px;white-space:nowrap}
.target b{background:var(--red);color:#fff;padding:0 10px}
.target .box{border:2px solid var(--ink);padding:0 8px}

.result-card{font-weight:900;line-height:1.15;white-space:nowrap}
.result-card .small{font-size:26px}
.result-card .big{font-size:48px;color:var(--red)}
.pass-a{left:30px;top:676px}
.pass-b{left:450px;top:676px}
.stamp{width:68px;height:68px;border-radius:50%;background:var(--red);opacity:.85}
.stamp-a{left:300px;top:690px}
.stamp-b{left:690px;top:690px}

.sec-title{font-weight:900;font-size:26px;color:var(--blue);border-left:8px solid var(--blue);padding-left:10px;white-space:nowrap}
.track-title{left:30px;top:782px}
.track-list{left:30px;top:826px;font-size:19px;font-weight:700;line-height:1.7;white-space:nowrap}
.grade-title{left:450px;top:782px}
.grade-row{left:450px;font-weight:700;font-size:17px;white-space:nowrap;line-height:1.2}
.grade-row .pt{color:var(--red);font-weight:900;font-size:36px}
.grade-row .avg{font-size:14px;color:var(--grey);display:block;margin-left:24px}
.row-jan{top:826px}
.row-jun{top:890px}
.gain{left:730px;top:944px;background:var(--red);color:var(--yellow);font-weight:900;font-size:24px;
  padding:2px 12px;border-radius:6px;transform:rotate(-8deg);white-space:nowrap}

.top-student{left:30px;top:982px;display:flex;flex-direction:column;gap:2px;white-space:nowrap}
.top-student .lead{font-weight:900;font-size:22px}
.top-student .jump{display:flex;align-items:baseline;gap:12px;font-weight:700;font-size:20px;padding-left:40px}
.top-student .jump .pt{color:var(--red);font-weight:900;font-size:40px;line-height:1.1}
.top-student .jump .pt.final{font-size:50px}

.banner{left:0;top:1078px;width:863px;height:40px;background:linear-gradient(90deg,var(--red),var(--orange));
  color:#fff;font-weight:900;font-size:22px;display:flex;align-items:center;justify-content:center;white-space:nowrap}
.banner em{font-style:normal;color:var(--yellow);font-size:28px;margin:0 2px}

.head-photo{left:30px;top:1126px;width:62px;height:70px;background:linear-gradient(180deg,#c9d3dc,#8e9aa6)}
.head-label{left:108px;top:1126px;background:var(--ink);color:#fff;font-weight:700;font-size:14px;padding:1px 10px;white-space:nowrap}
.head-label b{font-size:16px;margin-left:8px}
.message{left:108px;top:1152px;width:730px;font-size:13px;line-height:1.6}
</style>
</head>
<body>
<main class="flyer">
  <div class="abs hero-bg"></div>
  <div class="abs student-photo" role="img" aria-label="制服姿の女子生徒の写真"></div>

  <svg class="abs up-arrow" viewBox="0 0 440 200" aria-hidden="true">
    <path d="M0 190 Q220 165 400 40" fill="none" stroke="var(--red)" stroke-width="9"/>
    <polygon points="418,26 368,36 396,70" fill="var(--red)"/>
  </svg>
  <div class="abs score-lead">5教科合計250点が</div>
  <div class="abs score-big">400<small>点</small></div>
  <div class="abs score-ni">に</div>
  <div class="abs score-up">UP!!</div>

  <h1 class="abs headline">
    <span class="l1">本気で</span><br>
    <span class="l2">成績を</span><br>
    <span class="l3">あげたい子のための学習塾</span>
  </h1>

  <div class="abs brand-rule"></div>
  <div class="abs brand"><span class="brand-mark"></span><span class="brand-name">蒼翔舎</span></div>
  <div class="abs schools"><span>桐ヶ丘中学校</span><span>南峰中学校</span><span>南峰第二中学校</span></div>
  <div class="abs target"><span class="box">上記中学校へ進学予定の小学生</span>が対象の<b>高校受験専門塾</b></div>

  <div class="abs result-card pass-a"><div class="small">昨年度第3期生</div><div class="big">全員志望校</div></div>
  <div class="abs stamp stamp-a"></div>
  <div class="abs result-card pass-b"><div class="small">開校以来毎年</div><div class="big">青嶺高校</div></div>
  <div class="abs stamp stamp-b"></div>

  <h2 class="abs sec-title track-title">過去3年間の主な進学実績</h2>
  <p class="abs track-list">白浜高専、白浜高校、藤波高校、朝霧野工業<br>光陽工業専修、白浜緑丘、西千歳高校<br>白浜東萌、明徳学園、朝短附、琴葉女子<br>葉技大附属</p>

  <h2 class="abs sec-title grade-title">成績実績</h2>
  <div class="abs grade-row row-jan">1月峰陵模試 蒼翔舎生平均点 <span class="pt">317.8点</span><span class="avg">(県平均 265.3点)</span></div>
  <div class="abs grade-row row-jun">6月峰陵模試 蒼翔舎生平均点 <span class="pt">262.0点</span><span class="avg">(県平均 247.8点)</span></div>
  <div class="abs gain">55点UP!</div>

  <div class="abs top-student">
    <span class="lead">最も成績が上がった生徒は</span>
    <span class="jump">6月峰陵模試 <span class="pt">258点</span> ▶ 入試得点開示 <span class="pt final">391点</span></span>
  </div>

  <div class="abs banner">250点が<em>400点</em>に!真ん中から上位の指導を得意としています!</div>

  <div class="abs head-photo" role="img" aria-label="塾長の写真"></div>
  <div class="abs head-label">学習塾蒼翔舎 塾長<b>森川 遼</b></div>
  <p class="abs message">勉強が苦手な生徒から所謂進学校へ進む生徒まで、すべての生徒と卒業まで向き合ってきました。定員10人の小さい教室ながら、まさに3年間、生徒と肩を組むようにして勉強に取り組みました。</p>
</main>
</body>
</html>
```